Business Card design for construction company

I would like a business card design for a construction company - Harlow Constructions. I have attached the ai logo file for use. I would like the card to be very smart and clean and incorporate only white and the two colours in the logo. I would like the card to have two sides. One side can just have the logo, the other with the relevant information.

Target Market(s)

Building and Construction Clients

Industry/Entity Type

Business

Contact Information for Business Card

Name: Tom Pardoe
Company: Harlow Constructions Pty Limited
Address: 14 Mallee Crescent Carrow Vale 2093
Phone: 0427 531 068
Email: tomp@harlowbuild-example.com.au

Font styles to use
Serif
Sans Serif

Requirements
Must have
• Details noted above
• Logo as provided
• Colours as in logo
• Square edges
• A font that compliments the logo
Should not have
• Any colour other than white and those in logo
• Rounded edges

```html
<!DOCTYPE html>
<html lang="en">
<head>
<meta charset="utf-8">
<title>Harlow Constructions – Business Card</title>
<link rel="stylesheet" href="https://fonts.googleapis.com/css2?family=Michroma&display=swap">
<style>
  :root {
    --backdrop: #77726f;
    --card: #e6e6e6;
    --ink: #545658;
    --ink-dark: #47494b;
    --accent: #1b9bd7;
  }
  * { margin: 0; padding: 0; box-sizing: border-box; }
  html, body {
    width: 1200px;
    height: 1200px;
    overflow: hidden;
    background: var(--backdrop);
    font-family: "Michroma", sans-serif;
    color: var(--ink);
  }
  .card {
    position: absolute;
    left: 150px;
    width: 900px;
    height: 540px;
    background: var(--card);
  }
  .card--front { top: 46px; }
  .card--back { top: 614px; }

  .wordmark {
    display: flex;
    align-items: center;
    gap: 18px;
    white-space: nowrap;
    color: var(--ink);
    text-transform: uppercase;
  }
  .wordmark__dot {
    flex: none;
    background: var(--accent);
  }
  .card--front .wordmark {
    position: absolute;
    left: 0; right: 0; top: 0; bottom: 0;
    justify-content: center;
    font-size: 36px;
    letter-spacing: 2px;
  }
  .card--front .wordmark__dot { width: 16px; height: 16px; }

  .card--back .wordmark {
    position: absolute;
    left: 78px;
    top: 124px;
    font-size: 22px;
    letter-spacing: 1px;
    gap: 12px;
  }
  .card--back .wordmark__dot { width: 10px; height: 10px; }

  .rule {
    position: absolute;
    left: 78px;
    top: 186px;
    width: 744px;
    height: 3px;
    background: var(--ink);
  }
  .holder-name {
    position: absolute;
    right: 74px;
    top: 214px;
    font-size: 23px;
    letter-spacing: 4px;
    color: var(--ink-dark);
    -webkit-text-stroke: 0.6px var(--ink-dark);
    text-transform: uppercase;
  }
  .contacts {
    position: absolute;
    left: 78px;
    top: 371px;
    list-style: none;
  }
  .contact {
    display: flex;
    align-items: center;
    height: 32px;
    margin-bottom: 15px;
    font-size: 14px;
    letter-spacing: 3px;
    text-transform: uppercase;
    color: var(--ink-dark);
  }
  .contact__icon {
    width: 32px;
    height: 32px;
    margin-right: 20px;
    flex: none;
  }
  .contact--email { font-size: 12px; letter-spacing: 2.5px; }
</style>
</head>
<body>

<section class="card card--front" aria-label="Card front">
  <div class="wordmark">
    <span class="wordmark__dot" aria-hidden="true"></span>
    <span class="wordmark__name">Harlow Constructions</span>
  </div>
</section>

<section class="card card--back" aria-label="Card back">
  <div class="wordmark">
    <span class="wordmark__dot" aria-hidden="true"></span>
    <span class="wordmark__name">Harlow Constructions</span>
  </div>
  <div class="rule"></div>
  <p class="holder-name">Tom Pardoe</p>

  <ul class="contacts">
    <li class="contact contact--phone">
      <svg class="contact__icon" viewBox="0 0 32 32" aria-hidden="true">
        <circle cx="16" cy="16" r="16" fill="var(--ink)"/>
        <path d="M11.2 8.5c.6-.4 1.3-.3 1.7.3l1.6 2.6c.3.6.2 1.2-.3 1.6l-1 .8c.6 1.8 2.3 3.9 4.2 5l1-.9c.5-.4 1.1-.5 1.6-.1l2.5 1.7c.6.4.7 1.1.3 1.7-.9 1.4-2.2 2.4-3.6 2.1-4.5-1-8.5-5.4-9.2-9.8-.3-1.6.4-2.4 1.2-3z" fill="#eeeeee"/>
      </svg>
      <span>0427 531 068</span>
    </li>
    <li class="contact contact--email">
      <svg class="contact__icon" viewBox="0 0 32 32" aria-hidden="true">
        <circle cx="16" cy="16" r="16" fill="var(--ink)"/>
        <rect x="8.5" y="10.5" width="15" height="11" fill="none" stroke="#eeeeee" stroke-width="1.6"/>
        <path d="M8.5 10.5l7.5 6.5 7.5-6.5M8.5 21.5l5.5-5M23.5 21.5l-5.5-5" fill="none" stroke="#eeeeee" stroke-width="1.4"/>
      </svg>
      <span>tomp@harlowbuild-example.com.au</span>
    </li>
    <li class="contact contact--address">
      <svg class="contact__icon" viewBox="0 0 32 32" aria-hidden="true">
        <circle cx="16" cy="16" r="16" fill="var(--ink)"/>
        <path d="M16 7a6 6 0 0 0-6 6c0 4.5 6 12 6 12s6-7.5 6-12a6 6 0 0 0-6-6z" fill="#eeeeee"/>
        <circle cx="16" cy="13" r="2.3" fill="var(--ink)"/>
      </svg>
      <span>14 Mallee Crescent Carrow Vale 2093</span>
    </li>
  </ul>
</section>

</body>
</html>
```